Swift TECH Talentline by graduating students from college in two years

Based on the logo design, create stationary and business cards for
Dr. Velmor T Quenby, CEO, (555) 412-3076
and Lorna Pettigrew, Respresentative, (555) 238-6041
Address: 4197 Thistlemoor Lane, Brindlecove, VA 24517
Incorporate elelments of the logo

Target Market(s)

USA

Font styles to use
Other font styles liked:
• match with the logo type style

```html
<!DOCTYPE html>
<html lang="en">
<head>
<meta charset="utf-8">
<title>Swift TECH Talentline – Letterhead</title>
<link href="https://fonts.googleapis.com/css2?family=Arimo:wght@400;500&display=swap" rel="stylesheet">
<style>
  :root {
    --navy: #02205b;
    --gold: #f3c32c;
    --ink: #222222;
    --body: #333333;
    --backdrop: #e4e4e4;
    --paper: #ffffff;
    --sign-area: #eceef3;
  }
  * { margin: 0; padding: 0; box-sizing: border-box; }
  html, body {
    width: 1058px; height: 1200px; overflow: hidden;
    background: var(--backdrop);
    font-family: "Arimo", Arial, sans-serif;
  }
  .letterhead {
    position: absolute; left: 119px; top: 20px;
    width: 820px; height: 1160px;
    background: var(--paper);
  }
  .brand {
    position: absolute; left: 77px; top: 38px;
    width: 250px; height: 126px;
    display: flex; align-items: center; gap: 10px;
  }
  .brand-dot {
    width: 22px; height: 22px; border-radius: 50%;
    background: var(--gold); flex: none;
  }
  .brand-name {
    color: var(--navy); font-size: 19px; font-weight: 500;
    line-height: 1.2;
  }
  .contacts {
    position: absolute; right: 76px; top: 50px;
    text-align: right; color: var(--navy);
  }
  .contact-name { font-size: 17px; line-height: 24px; }
  .contact-phone {
    font-size: 15px; line-height: 22px; color: var(--ink);
    display: flex; justify-content: flex-end; align-items: center; gap: 5px;
  }
  .contact-phone svg { width: 16px; height: 14px; }
  .contact + .contact { margin-top: 8px; }
  .letter-meta {
    position: absolute; left: 77px; right: 79px; top: 320px;
    display: flex; justify-content: space-between;
    font-size: 15.5px; font-weight: 500; color: var(--ink);
  }
  .letter-body {
    position: absolute; left: 77px; right: 79px; top: 374px;
    font-size: 14.5px; line-height: 24.8px; color: var(--body);
    text-align: justify;
  }
  .letter-body p { margin-bottom: 24px; }
  .letter-body p.gap-large { margin-bottom: 50px; }
  .signature {
    position: absolute; left: 77px; top: 1000px;
    width: 208px; height: 46px;
    background: var(--sign-area); border-radius: 4px;
  }
  .footer-address {
    position: absolute; left: 175px; top: 1108px;
    font-size: 15px; color: var(--ink);
  }
  .footer-stripe {
    position: absolute; left: 532px; top: 1113px;
    width: 288px; height: 10px;
  }
</style>
</head>
<body>
  <main class="letterhead">
    <div class="brand">
      <span class="brand-dot"></span>
      <span class="brand-name">Swift TECH Talentline</span>
    </div>

    <div class="contacts">
      <div class="contact">
        <div class="contact-name">Dr. Velmor T Quenby, CEO</div>
        <div class="contact-phone">
          <svg viewBox="0 0 16 14" aria-hidden="true"><path fill="#02205b" d="M1 4.5C1 2 4 1 8 1s7 1 7 3.5v1h-3.5v-1.5h-7v1.5H1z"/><path fill="#02205b" d="M4 6h8l2.5 7h-13z"/><circle cx="8" cy="9.5" r="2" fill="#fff"/></svg>
          (555) 412-3076
        </div>
      </div>
      <div class="contact">
        <div class="contact-name">Lorna Pettigrew, Respresentative</div>
        <div class="contact-phone">
          <svg viewBox="0 0 16 14" aria-hidden="true"><path fill="#02205b" d="M1 4.5C1 2 4 1 8 1s7 1 7 3.5v1h-3.5v-1.5h-7v1.5H1z"/><path fill="#02205b" d="M4 6h8l2.5 7h-13z"/><circle cx="8" cy="9.5" r="2" fill="#fff"/></svg>
          (555) 238-6041
        </div>
      </div>
    </div>

    <div class="letter-meta">
      <span class="recipient">Dr. Velmor T Quenby</span>
      <span class="date">Date: 15-12-2025</span>
    </div>

    <div class="letter-body">
      <p class="gap-large">Lorem Ipsum is simply dummy text of the printing and typesetting industry. Lorem Ipsum has been the industry's standard dummy text ever since the 1500s, when an unknown printer took a galley of type and scrambled it to make a type specimen book. It has survived not only five centuries, but also the leap into electronic typesetting, remaining essentially unchanged. It was popularised in the 1960s with the release of Typeline sheets containing Lorem Ipsum passages, and more recently with desktop publishing software like Pagecraft Studio including versions of Lorem Ipsum.</p>
      <p>Contrary to popular belief, Lorem Ipsum is not simply random text. It has roots in a piece of classical Latin literature from 45 BC, making it over 2000 years old. Harlan Whitcombe, a Latin professor at Ashgrove-Linden College in Virginia, looked up one of the more obscure Latin words, consectetur, from a Lorem Ipsum passage, and going through the cites of the word in classical literature, discovered the undoubtable source. Lorem Ipsum comes from sections 1.10.32 and 1.10.33 of "de Finibus Bonorum et Malorum" (The Extremes of Good and Evil) by Marcellus, written in 45 BC. This book is a treatise on the theory of ethics, very popular during the Renaissance. The first line of Lorem Ipsum, "Lorem ipsum dolor sit amet..", comes from a line in section 1.10.32.</p>
      <p>There are many variations of passages of Lorem Ipsum available, but the majority have suffered alteration in some form, by injected humour, or randomised words which don't look even slightly believable. If you are going to use a passage.</p>
      <p class="closing">Regards,</p>
    </div>

    <div class="signature" role="img" aria-label="Handwritten signature of Dr. Velmor T Quenby"></div>

    <div class="footer-address">4197 Thistlemoor Lane, Brindlecove, VA 24517</div>
    <svg class="footer-stripe" viewBox="0 0 288 10" preserveAspectRatio="none" aria-hidden="true">
      <polygon points="4,0 32,0 28,10 0,10" fill="var(--navy)"/>
      <polygon points="38,0 64,0 60,10 34,10" fill="var(--gold)"/>
      <polygon points="70,0 288,0 288,10 66,10" fill="var(--navy)"/>
    </svg>
  </main>
</body>
</html>
```